Bright Feather Glow Masterclass

This book accompanies a video workshop. The book explains who our guardian angels are, what is their purpose, how to connect with them for wisdom & guidance. How to manifest what we world like bring into our lives by asking the Angels. The book contains meditation exercises, lots of information and fun facts about how our angels give us messages and guidance and how to become more intuitive. How to use angel oracle cards to receive guidance from our angels.
I'm quite an upbeat, happy person, so the book is written very warmly and is a collection of all the information that out ther, drawn together neatly by me, with my own unique take on all things angelic. Along with personal stories and anecdotes about how and why I became interested in angels and what they have taught me. It's fun, fresh, lighthearted and modern. Not at all serious, just extremely uplifting and positive, so I would really like the cover to reflect this.
Updates

Target Market(s)

Anyone who is interested in angels. From my loopnest page activity I find it is mostly women of all ages who are interested in angels

Font styles to use
Serif
Sans Serif
Script

Colors
ea8dbb
f04a50
e667a6
e34197
85abd2
886aae
b7a5cd
6b449b
fbee3e

Requirements
Must have
• A more feminine appeal
• Look quite modern & upbeat but also calming and open
• I would like it to look etherel in some way. I definitely dont want something that looks like a cartoon or clip art
Should not have
• No dark colours or sinister imagery. I don't want people to feel like thus can't do the & it's only special people who can connect with their angels
• No haunting imagery!

```html
<!DOCTYPE html>
<html lang="en">
<head>
<meta charset="utf-8">
<title>Bright Feather Glow Masterclass — Book Cover</title>
<link href="https://fonts.googleapis.com/css2?family=Questrial&family=Pinyon+Script&family=Parisienne&display=swap" rel="stylesheet">
<style>
  :root {
    --indigo: #3a3fd6;
    --deep-blue: #3d48e6;
    --lavender: #c7a8ef;
    --pink-mist: #efcdf2;
    --butter: #fdf8bf;
    --aqua: #92e9f8;
    --sky: #7fb3f2;
    --mint-type: #8ff0e6;
    --ice-type: #a9f2ff;
    --white: #ffffff;
  }
  html, body {
    margin: 0;
    padding: 0;
    width: 1000px;
    height: 1200px;
    overflow: hidden;
    background: var(--white);
  }
  .cover {
    position: relative;
    width: 1000px;
    height: 1200px;
    overflow: hidden;
    font-family: 'Questrial', 'Century Gothic', sans-serif;
  }
  .cover__wash {
    position: absolute;
    inset: 0;
    width: 1000px;
    height: 1200px;
  }
  .author {
    position: absolute;
    top: 100px;
    left: 0;
    width: 1000px;
    text-align: center;
    font-size: 47px;
    letter-spacing: 1px;
    color: var(--indigo);
    margin: 0;
  }
  .title {
    margin: 0;
    font-weight: normal;
  }
  .title__lead {
    position: absolute;
    top: 320px;
    left: 140px;
    font-size: 74px;
    color: var(--mint-type);
    letter-spacing: 1px;
    text-shadow: 0 0 8px rgba(255,255,255,.6);
  }
  .title__script {
    position: absolute;
    top: 380px;
    left: 230px;
    font-family: 'Pinyon Script', cursive;
    font-size: 190px;
    line-height: 1;
    color: var(--white);
    text-shadow: 0 0 10px rgba(170,190,255,.9), 0 0 22px rgba(150,170,255,.6);
  }
  .title__main {
    position: absolute;
    top: 568px;
    left: 600px;
    font-size: 112px;
    color: var(--ice-type);
    text-shadow: 0 0 10px rgba(255,255,255,.7);
  }
  .title__tail {
    position: absolute;
    top: 678px;
    left: 580px;
    font-size: 50px;
    letter-spacing: 2px;
    color: var(--ice-type);
    text-shadow: 0 0 8px rgba(255,255,255,.7);
  }
  .subtitle {
    position: absolute;
    top: 826px;
    left: 0;
    width: 1000px;
    text-align: center;
    font-size: 30px;
    letter-spacing: 1px;
    color: var(--indigo);
    margin: 0;
  }
  .tagline {
    position: absolute;
    left: 0;
    top: 1030px;
    width: 1000px;
    height: 140px;
    margin: 0;
    color: var(--white);
  }
  .tagline__lead {
    position: absolute;
    left: 72px;
    top: 42px;
    font-size: 19px;
  }
  .tagline__script {
    position: absolute;
    left: 140px;
    top: 2px;
    font-family: 'Parisienne', cursive;
    font-size: 60px;
    white-space: nowrap;
  }
  .tagline__amp {
    font-family: 'Questrial', sans-serif;
    font-size: 22px;
  }
  .tagline__tail {
    position: absolute;
    right: 34px;
    top: 98px;
    font-size: 20px;
  }
</style>
</head>
<body>
<main class="cover">
  <svg class="cover__wash" viewBox="0 0 1000 1200" role="img" aria-label="Soft watercolour wash of layered curved bands, blue at the edges through lavender and aqua to a pale yellow glow in the centre">
    <defs>
      <linearGradient id="wash-base" x1="0" y1="0" x2="0" y2="1">
        <stop offset="0" stop-color="#5258ee"/>
        <stop offset="0.12" stop-color="#a996f0"/>
        <stop offset="0.26" stop-color="#e6c4f2"/>
        <stop offset="0.45" stop-color="#fbf3c6"/>
        <stop offset="0.6" stop-color="#f4f8c4"/>
        <stop offset="0.72" stop-color="#b8f0f0"/>
        <stop offset="0.82" stop-color="#8fe4f8"/>
        <stop offset="0.92" stop-color="#7fa8f0"/>
        <stop offset="1" stop-color="#4450e8"/>
      </linearGradient>
      <radialGradient id="wash-edge" cx="0.5" cy="0.47" r="0.72">
        <stop offset="0.55" stop-color="#3d48e6" stop-opacity="0"/>
        <stop offset="1" stop-color="#3d48e6" stop-opacity="0.85"/>
      </radialGradient>
      <filter id="soften"><feGaussianBlur stdDeviation="5"/></filter>
    </defs>
    <rect class="wash__base" width="1000" height="1200" fill="url(#wash-base)"/>
    <g class="wash__bands" filter="url(#soften)" fill="none" stroke-linecap="round">
      <path d="M-40 120 C 250 20, 700 10, 1040 110" stroke="#8a7bf0" stroke-width="40" opacity=".5"/>
      <path d="M-40 230 C 260 120, 720 110, 1040 210" stroke="#d7b0f2" stroke-width="50" opacity=".55"/>
      <path d="M-40 330 C 280 230, 700 220, 1040 300" stroke="#f0c8f0" stroke-width="40" opacity=".45"/>
      <path d="M-40 830 C 300 950, 700 950, 1040 860" stroke="#a6ecf6" stroke-width="50" opacity=".55"/>
      <path d="M-40 930 C 300 1040, 700 1040, 1040 950" stroke="#88c8f6" stroke-width="45" opacity=".55"/>
      <path d="M-40 1030 C 300 1130, 700 1130, 1040 1050" stroke="#6c86ee" stroke-width="45" opacity=".5"/>
    </g>
    <ellipse class="wash__glow" cx="500" cy="560" rx="440" ry="300" fill="#fdf9c2" opacity=".55" filter="url(#soften)"/>
    <rect class="wash__edge" width="1000" height="1200" fill="url(#wash-edge)"/>
  </svg>

  <p class="author">MIRELA HARTWELL</p>

  <h1 class="title">
    <span class="title__lead">bright feather</span>
    <span class="title__script">Glow</span>
    <span class="title__main">master</span>
    <span class="title__tail">CLASS</span>
  </h1>

  <p class="subtitle">CONNECT WITH YOUR ANGELS</p>

  <p class="tagline">
    <span class="tagline__lead">Bring</span>
    <span class="tagline__script">love, healing, <span class="tagline__amp">&amp;</span> divine guidance</span>
    <span class="tagline__tail">to every area of your life</span>
  </p>
</main>
</body>
</html>
```